New Website for Belcourt Manor at www.belcourt.com.au

A new logo has been designed (through pixel forge) and we now want to align the look and feel of our website at www.belcourt.com.au to the new logo. The content and page names (e.g. Grounds) will remain largely unchanged for the new site, so please submit a new look "Home" page, using our new logo, current text and any photos you choose from the existing gallery at our website. I have also attached the current "Home" page photos.

Industry/Entity Type

Accommodation

Number of Pages Required

1 page

Requirements
Must have
• Logo to be presented on white background.

```html
<!DOCTYPE html>
<html lang="en">
<head>
<meta charset="utf-8">
<title>Belcourt Manor – Home</title>
<link rel="stylesheet" href="https://fonts.googleapis.com/css2?family=Montserrat:wght@300;400;500;600&display=swap">
<style>
  :root {
    --blue: #0763ad;
    --blue-dark: #04467d;
    --yellow: #fbd94a;
    --ink: #1a1a1a;
    --rule: #d6d6d6;
    --white: #ffffff;
  }
  * { margin: 0; padding: 0; box-sizing: border-box; }
  html, body { width: 1200px; height: 1200px; overflow: hidden; background: var(--white); }
  body { font-family: "Montserrat", sans-serif; color: var(--ink); position: relative; }

  .site-header { position: absolute; left: 88px; top: 0; width: 1024px; height: 96px; }
  .brand { position: absolute; left: 44px; top: 30px; display: flex; align-items: center; gap: 10px; }
  .brand-dot { width: 26px; height: 26px; border-radius: 50%; background: var(--yellow); }
  .brand-name { font-size: 26px; font-weight: 500; color: var(--blue); letter-spacing: 0.5px; }

  .address { position: absolute; right: 112px; top: 16px; font-size: 13.5px; line-height: 22.5px; padding-left: 17px; white-space: nowrap; }
  .address svg { position: absolute; left: 0; top: 4px; }
  .connect { position: absolute; left: 924px; top: 14px; height: 69px; border-left: 1px solid var(--rule); padding-left: 10px; font-size: 11px; line-height: 16px; white-space: nowrap; }
  .connect .social { display: block; width: 26px; height: 26px; border: 1.6px solid var(--blue); border-radius: 50%; margin: 5px 0 0 11px; }

  .main-nav { position: absolute; left: 88px; top: 96px; width: 1024px; height: 43px; background: var(--blue); display: flex; padding-left: 50px; }
  .main-nav a { color: var(--white); text-decoration: none; font-size: 11px; font-weight: 600; letter-spacing: 0.2px; line-height: 43px; padding: 0 13px; white-space: nowrap; }
  .main-nav a.current { background: var(--yellow); color: var(--ink); padding: 0 19px; margin-right: 2px; }

  .hero { position: absolute; left: 88px; top: 139px; width: 1024px; height: 470px; overflow: hidden; }
  .hero-photo { position: absolute; inset: 0; background: linear-gradient(180deg, #5f8a4a 0%, #d7a95a 25%, #e7c96b 45%, #c86a3f 60%, #8c8a82 75%, #7d7b76 100%); }
  .hero-wave { position: absolute; left: 0; bottom: 0; }
  .slide-arrow { position: absolute; top: 184px; width: 29px; height: 68px; background: rgba(40,40,40,0.55); }
  .slide-arrow.prev { left: 0; }
  .slide-arrow.next { right: 0; }
  .slide-arrow svg { position: absolute; left: 8px; top: 14px; }

  .intro { position: absolute; left: 88px; top: 636px; width: 1024px; text-align: center; }
  .intro h1 { font-size: 38px; font-weight: 300; letter-spacing: 1px; line-height: 48px; }
  .title-rule { position: relative; width: 776px; height: 1px; background: var(--rule); margin: 10px auto 20px; }
  .title-rule::after { content: ""; position: absolute; left: 380px; top: -8px; width: 16px; height: 8px; border-radius: 8px 8px 0 0; background: var(--yellow); }
  .intro p { font-size: 14.5px; line-height: 26px; margin: 0 auto 10px; width: 950px; }
  .intro a { color: var(--blue); font-style: italic; text-decoration: none; }

  .feature { position: absolute; left: 88px; top: 947px; width: 1024px; height: 253px; background: var(--blue); overflow: hidden; }
  .feature-edge { position: absolute; left: 0; top: 0; width: 526px; height: 253px; background: var(--blue-dark); clip-path: polygon(0 0, 427px 0, 526px 253px, 0 253px); }
  .feature-photo { position: absolute; left: 0; top: 0; width: 520px; height: 253px; background: linear-gradient(135deg, #efe3c2 0%, #d8c59a 45%, #b98b5c 75%, #6a4a34 100%); clip-path: polygon(0 0, 425px 0, 520px 253px, 0 253px); }
  .feature-body { position: absolute; left: 498px; top: 36px; color: var(--white); }
  .feature-body h2 { font-size: 35px; font-weight: 300; letter-spacing: 1px; line-height: 40px; margin-bottom: 12px; }
  .feature-list { list-style: none; font-size: 13.5px; line-height: 21.5px; }
  .feature-list li { position: relative; padding-left: 16px; margin-bottom: 11px; white-space: nowrap; }
  .feature-list li::before { content: "»"; position: absolute; left: 0; top: -1px; font-weight: 600; }
</style>
</head>
<body>
  <header class="site-header">
    <div class="brand"><span class="brand-dot"></span><span class="brand-name">Belcourt Manor</span></div>
    <div class="address">
      <svg width="9" height="13" viewBox="0 0 9 13"><path d="M4.5 0C2 0 0 2 0 4.5 0 8 4.5 13 4.5 13S9 8 9 4.5C9 2 7 0 4.5 0z" fill="#0763ad"/><circle cx="4.5" cy="4.5" r="1.7" fill="#fff"/></svg>
      42 Belcourt Drive<br>Marlow Ridge, Gold Coast<br>Queensland, Australia
    </div>
    <div class="connect">Connect<br>with us:<span class="social"></span></div>
  </header>

  <nav class="main-nav">
    <a class="current">Main</a><a>Mansion</a><a>Bedrooms</a><a>Options</a><a>Hare and Heron</a><a>Grounds</a><a>Location</a><a>Gallery</a><a>Contact</a><a>Availability</a><a>DIY Weddings</a>
  </nav>

  <section class="hero">
    <div class="hero-photo" role="img" aria-label="Aerial photo of the yellow manor with red tile roofs, palm trees and gravel forecourt"></div>
    <span class="slide-arrow prev"><svg width="12" height="40" viewBox="0 0 12 40"><path d="M10 2 Q2 20 10 38" stroke="#fff" stroke-width="2" fill="none"/></svg></span>
    <span class="slide-arrow next"><svg width="12" height="40" viewBox="0 0 12 40"><path d="M2 2 Q10 20 2 38" stroke="#fff" stroke-width="2" fill="none"/></svg></span>
    <svg class="hero-wave" width="1024" height="80" viewBox="0 0 1024 80" preserveAspectRatio="none">
      <path d="M0 28 Q200 -10 480 32 Q800 82 1024 0 L1024 80 L0 80 Z" fill="#0763ad"/>
      <path d="M0 34 Q200 4 480 44 Q800 96 1024 40 L1024 80 L0 80 Z" fill="#ffffff"/>
    </svg>
  </section>

  <section class="intro">
    <h1>PALATIAL ESTATE AND LUXURY RESORT</h1>
    <div class="title-rule"></div>
    <p>On over 2 manicured garden acres, Belcourt Manor is a unique Gold Coast estate, centrally located in the prestigious rural suburb of Marlow Ridge.&nbsp; <a>More about our Location</a></p>
    <p>The estate features a grand mansion, private pub (The Hare and Heron), sparkling resort pool, tennis court and playground.</p>
    <p>Magnificent properties rarely feel so warm and welcoming – so browse away and visit our <a>photo gallery</a><br>– and we look forward to having you stay as our guests.</p>
    <p>For prices, availability and guest reviews, <a>visit StayNest.</a></p>
  </section>

  <section class="feature">
    <div class="feature-edge"></div>
    <div class="feature-photo" role="img" aria-label="Interior photo of the high-ceilinged lounge with fireplace and leather sofas"></div>
    <div class="feature-body">
      <h2>GRAND MANSION</h2>
      <ul class="feature-list">
        <li>Regal entrance and sweeping staircase</li>
        <li style="margin-left:14px">Stately lounge or ballroom with 18 foot panelled ceiling and gas-driven<br>fireplace – fondly referred to as “The Lindqvist Room”</li>
        <li style="margin-left:38px">Elegant formal dining room</li>
        <li style="margin-left:52px">Large open living area</li>
        <li style="margin-left:65px">New Guinea Rosewood gourmet kitchen with walk-in pantry</li>
      </ul>
    </div>
  </section>
</body>
</html>
```